PKD Business Card

Looking for a business card for my restaurant group I own. Four different concepts:

Bramblecrest Alehall
Vellory Alehall
Tamrack's Stone Hearth Kitchen
Cobblestead Patty Works

Card doesn't need to include all the logos.

```html
<!DOCTYPE html>
<html lang="en">
<head>
<meta charset="UTF-8">
<title>PKD Business Card</title>
<link href="https://fonts.googleapis.com/css2?family=Poppins:wght@400;500;600&display=swap" rel="stylesheet">
<style>
  :root {
    --backdrop: #232122;
    --card-white: #ffffff;
    --card-grey: #707174;
    --gold: #d2ae6c;
    --ink: #545454;
    --light: #ffffff;
  }
  * { margin: 0; padding: 0; box-sizing: border-box; }
  html, body {
    width: 1125px;
    height: 1200px;
    overflow: hidden;
    background: var(--backdrop);
    font-family: "Poppins", sans-serif;
  }
  .canvas { position: relative; width: 1125px; height: 1200px; }

  .card {
    position: absolute;
    left: 150px;
    width: 824px;
    height: 470px;
  }
  .card--front { top: 106px; background: var(--card-white); }
  .card--back  { top: 638px; background: var(--card-grey); }

  /* Front */
  .name-band {
    position: absolute;
    left: 0; top: 142px;
    width: 505px; height: 68px;
    background: var(--gold);
    color: var(--light);
    padding: 6px 0 0 45px;
  }
  .name-band__name { font-size: 30px; font-weight: 600; line-height: 36px; }
  .name-band__title { font-size: 20px; font-weight: 400; line-height: 22px; }

  .brand {
    position: absolute;
    left: 505px; top: 44px;
    width: 278px;
    text-align: center;
    color: var(--gold);
    font-weight: 500;
  }
  .brand__initials { font-size: 72px; line-height: 80px; letter-spacing: 4px; }
  .brand__name {
    margin-top: 14px;
    font-size: 21px;
    line-height: 28px;
    letter-spacing: 3px;
    text-transform: uppercase;
  }

  .contact {
    position: absolute;
    color: var(--ink);
    font-size: 20px;
    line-height: 26px;
  }
  .contact--direct { left: 47px; top: 330px; }
  .contact--office { right: 46px; top: 352px; text-align: right; }
  .contact__web { letter-spacing: 1px; }

  /* Back */
  .back-mark {
    position: absolute;
    left: 0; right: 0; top: 92px;
    text-align: center;
    color: var(--light);
    font-size: 200px;
    font-weight: 600;
    line-height: 200px;
    letter-spacing: 6px;
  }
  .back-url {
    position: absolute;
    left: 0; right: 0; top: 388px;
    text-align: center;
    color: var(--light);
    font-size: 19px;
    letter-spacing: 4.5px;
  }
</style>
</head>
<body>
<main class="canvas">
  <section class="card card--front">
    <div class="name-band">
      <p class="name-band__name">Daniel Reyes</p>
      <p class="name-band__title">President</p>
    </div>
    <div class="brand">
      <p class="brand__initials">PKD</p>
      <p class="brand__name">Parkdale<br>Hospitality Group</p>
    </div>
    <div class="contact contact--direct">
      <p>P. 555-214-0193</p>
      <p>M. 555-618-2740</p>
      <p>F. 555-307-4862</p>
      <p>name@parkdalehospitality.com</p>
    </div>
    <div class="contact contact--office">
      <p>2140 Alder Ridge Road</p>
      <p>Anchorage, Alaska 99501</p>
      <p class="contact__web">parkdalehospitality.com</p>
    </div>
  </section>

  <section class="card card--back">
    <p class="back-mark">PKD</p>
    <p class="back-url">WWW.PARKDALEHOSPITALITY.COM</p>
  </section>
</main>
</body>
</html>
```